Flyer-Design für Hersteller von ökologischen Werbemitteln aus Papier/Karton
Zielgruppe
Wir machen ökologische Werbemittel aus Papier/Karton wie Parkscheiben, Drehscheiben usw.
Aufgabenstellung
Wir suchen den Content für einen Falzflyer im Format 220 x 150 mm (offen) bzw. 110 x 150 mm (geschlossen) mit folgenden Inhalten.
Seite 1: Frei/Leer
Seite 2 (Innen) : Speisekarte Pizzeria Valtoro Teil I (einfach ein paar Pizzen)
Seite 3 (Innen): Speiseikarte Pizzeria Valtoro Teil II (einfach ein paar Nudelgerichte)
Seite 4 (Rückseite): Zehn leere Felder für Stempel Pizzeria Valtoro (nach zehn Stempeln bekommt der Käufer eine Pizza gratis)
Das gesamte Design/Layout in einem Pizzierastyle.

```html
<!DOCTYPE html>
<html lang="de">
<head>
<meta charset="utf-8">
<title>Pizzeria Valtoro – Speisekarte und Bonus-Pass</title>
<link href="https://fonts.googleapis.com/css2?family=Yellowtail&family=Roboto+Condensed:wght@400&display=swap" rel="stylesheet">
<style>
  :root {
    --page-bg: #ffffff;
    --board-dark: #0e0e0e;
    --board-mid: #2b2b2b;
    --accent: #c9471b;
    --chalk: #f4f4f4;
    --stamp-fill: #8a8a8a;
    --stamp-edge: #ffffff;
    --crust: #d9a15e;
    --tomato: #b8432a;
  }
  html, body { margin: 0; padding: 0; }
  body {
    width: 1200px; height: 3128px; overflow: hidden;
    background: var(--page-bg); position: relative;
    font-family: "Roboto Condensed", "Arial Narrow", sans-serif;
  }
  .board {
    position: absolute;
    background: radial-gradient(ellipse at 45% 35%, var(--board-mid) 0%, #1a1a1a 45%, var(--board-dark) 100%);
    overflow: hidden;
  }
  .menu-spread { left: 65px; top: 1152px; width: 1092px; height: 743px; }
  .pizza-photo {
    position: absolute; left: 0; top: 0; width: 272px; height: 214px;
    border-bottom-right-radius: 272px 214px;
    background: radial-gradient(circle at 35% 40%, var(--tomato) 0%, #c97a3e 40%, var(--crust) 70%, #8b5a2b 100%);
  }
  .menu-title {
    position: absolute; left: 166px; top: 170px; margin: 0;
    font-family: "Yellowtail", cursive; font-weight: 400;
    font-size: 84px; line-height: 1; color: var(--accent);
    white-space: nowrap; transform: scaleX(0.85); transform-origin: left top;
  }
  .menu-list { position: absolute; margin: 0; padding: 0; list-style: none; }
  .menu-list--pizza { left: 29px; top: 308px; width: 492px; }
  .menu-list--pasta { left: 574px; top: 44px; width: 492px; }
  .dish { height: 67px; color: var(--chalk); }
  .dish-line { display: flex; align-items: baseline; }
  .dish-name, .dish-price {
    font-family: "Yellowtail", cursive; font-size: 24px; line-height: 30px; white-space: nowrap;
  }
  .dish-leader { flex: 1; min-width: 10px; border-bottom: 2px dotted var(--chalk); margin: 0 2px; transform: translateY(-6px); }
  .dish-desc { font-size: 15px; line-height: 18px; margin-top: 2px; white-space: nowrap; }

  .bonus-card { left: 338px; top: 2050px; width: 546px; height: 743px; }
  .bonus-title {
    position: absolute; left: 0; right: 0; top: 20px; margin: 0; text-align: center;
    font-family: "Yellowtail", cursive; font-weight: 400; font-size: 54px; line-height: 1; color: var(--accent);
    white-space: nowrap;
  }
  .bonus-text {
    position: absolute; left: 40px; right: 26px; top: 86px; margin: 0;
    font-size: 15px; line-height: 19px; color: var(--chalk);
  }
  .stamp-grid {
    position: absolute; left: 30px; top: 146px;
    display: grid; grid-template-columns: 227px 227px; column-gap: 34px; row-gap: 20px;
  }
  .stamp-field {
    height: 104px; box-sizing: border-box; border-radius: 14px;
    border: 4px solid var(--stamp-edge); background: var(--stamp-fill);
  }
  .brand-mark {
    position: absolute; left: 40px; top: 640px; width: 76px; height: 76px; border-radius: 50%;
    background: var(--accent); color: var(--chalk);
    display: flex; align-items: center; justify-content: center; font-size: 15px;
  }
  .bonus-phone {
    position: absolute; left: 178px; top: 640px; margin: 0;
    font-family: "Yellowtail", cursive; font-size: 58px; line-height: 1; color: var(--accent);
    white-space: nowrap; transform: scaleX(0.72); transform-origin: left top;
  }
  .bonus-address {
    position: absolute; left: 168px; top: 708px; margin: 0; font-size: 14px; line-height: 18px;
    color: var(--chalk); white-space: nowrap;
  }
</style>
</head>
<body>
  <section class="board menu-spread" aria-label="Speisekarte Innenseiten">
    <div class="pizza-photo" role="img" aria-label="Foto einer Pizza mit Tomaten, Mozzarella, Basilikum und Oliven"></div>
    <h1 class="menu-title">Pizza &amp; Pasta</h1>

    <ul class="menu-list menu-list--pizza">
      <li class="dish"><div class="dish-line"><span class="dish-name">Margerita</span><span class="dish-leader"></span><span class="dish-price">€ 5,20</span></div><div class="dish-desc">Tomaten, Käse, Oregano</div></li>
      <li class="dish"><div class="dish-line"><span class="dish-name">Romana</span><span class="dish-leader"></span><span class="dish-price">€5,90</span></div><div class="dish-desc">Tomaten, Käse, Sardinen</div></li>
      <li class="dish"><div class="dish-line"><span class="dish-name">Gemüsepizza</span><span class="dish-leader"></span><span class="dish-price">€ 5,90</span></div><div class="dish-desc">Mais, Zwiebel, Champignons, Spargel und Käse</div></li>
      <li class="dish"><div class="dish-line"><span class="dish-name">Spinaci</span><span class="dish-leader"></span><span class="dish-price">€ 6, 20</span></div><div class="dish-desc">Tomaten, Käse, Spinat</div></li>
      <li class="dish"><div class="dish-line"><span class="dish-name">Salami</span><span class="dish-leader"></span><span class="dish-price">€ 6,50</span></div><div class="dish-desc">Tomaten, Käse, Salami</div></li>
      <li class="dish"><div class="dish-line"><span class="dish-name">Al Tonno</span><span class="dish-leader"></span><span class="dish-price">€ 6,30</span></div><div class="dish-desc">Tomaten, Käse, Thunfisch</div></li>
    </ul>

    <ul class="menu-list menu-list--pasta">
      <li class="dish"><div class="dish-line"><span class="dish-name">Spaghetti Napoli</span><span class="dish-leader"></span><span class="dish-price">€ 6,50</span></div><div class="dish-desc">mit Tomaten und Knoblauch</div></li>
      <li class="dish"><div class="dish-line"><span class="dish-name">Spaghetti Bolognese</span><span class="dish-leader"></span><span class="dish-price">€ 6,70</span></div><div class="dish-desc">mit Fleischsauce</div></li>
      <li class="dish"><div class="dish-line"><span class="dish-name">Spaghetti Aglio</span><span class="dish-leader"></span><span class="dish-price">€ 6,50</span></div><div class="dish-desc">mit Knoblauch, Öl, Pfefferoni</div></li>
      <li class="dish"><div class="dish-line"><span class="dish-name">Spaghetti Diavolo</span><span class="dish-leader"></span><span class="dish-price">€ 6,50</span></div><div class="dish-desc">mit Tomaten, Schinken, Pfefferoni</div></li>
      <li class="dish"><div class="dish-line"><span class="dish-name">Spaghetti ala Carbonara</span><span class="dish-leader"></span><span class="dish-price">€ 6,50</span></div><div class="dish-desc">mit Speck, Ei, Schlagobers</div></li>
      <li class="dish"><div class="dish-line"><span class="dish-name">Spaghetti Della Casa</span><span class="dish-leader"></span><span class="dish-price">€ 6,50</span></div><div class="dish-desc">mit Tomaten, Paprika, Schafskäse</div></li>
      <li class="dish"><div class="dish-line"><span class="dish-name">Gnocchi al Ragù</span><span class="dish-leader"></span><span class="dish-price">€ 6,50</span></div><div class="dish-desc">mit Fleischsauce</div></li>
      <li class="dish"><div class="dish-line"><span class="dish-name">Gnocchi Diavolo</span><span class="dish-leader"></span><span class="dish-price">€ 7,00</span></div><div class="dish-desc">Kartoffelnockern mit Tomaten, Schinken, Pfefferoni</div></li>
      <li class="dish"><div class="dish-line"><span class="dish-name">Gnocchi Alla Chef</span><span class="dish-leader"></span><span class="dish-price">€ 7,00</span></div><div class="dish-desc">mit Gorgonzolakäse und Schinken</div></li>
      <li class="dish"><div class="dish-line"><span class="dish-name">Gnocchi In Verde</span><span class="dish-leader"></span><span class="dish-price">€ 6,50</span></div><div class="dish-desc">mit Blattspinat</div></li>
    </ul>
  </section>

  <section class="board bonus-card" aria-label="Bonus-Pass Rückseite">
    <h2 class="bonus-title">Bonus-Pass</h2>
    <p class="bonus-text">Für jede Pizza oder Pasta erhalten Sie einen Stempel. Wenn diese Bonuskarte voll ist, erhalten Sie eine Pizza oder Pasta gratis!</p>
    <div class="stamp-grid">
      <div class="stamp-field"></div><div class="stamp-field"></div>
      <div class="stamp-field"></div><div class="stamp-field"></div>
      <div class="stamp-field"></div><div class="stamp-field"></div>
      <div class="stamp-field"></div><div class="stamp-field"></div>
    </div>
    <div class="brand-mark">Valtoro</div>
    <p class="bonus-phone">Tel. 04711 58 302</p>
    <p class="bonus-address">Pizzeria Valtoro | Lindenweg 42 | 28719 Brakendorf</p>
  </section>
</body>
</html>
```